Revamp my web site design

Willowbrook Care Practitioners is a not for profit organisation focused on providing emotional support and counselling services to those with cancer or affected by cancer including those bereaved.

Our web site is intended to welcome suffers to engage with the services of its members and is also provided to encourage additional counsellors to join the organisation and then supports its members with access to materials and courses to extend their professional development.

We have a limited budget and seek to not only improve the attractiveness of the site but also improve the functionality and ease of maintenance. Especially site administrtaion should allow for uploading documents, adding new members, news and events easily.

Existing site is www.willowbrookcare.com.au

```html
<!DOCTYPE html>
<html lang="en">
<head>
<meta charset="utf-8">
<title>Willowbrook Care Practitioners</title>
<link rel="stylesheet" href="https://fonts.googleapis.com/css2?family=Gelasio:ital,wght@0,400;1,400;1,700&family=Roboto:wght@400;700&family=Lora:ital@1&display=swap">
<style>
:root{
  --page:#ffffff;
  --ink:#111111;
  --body:#555555;
  --footer:#222222;
  --base:#0b0b0b;
  --footer-text:#eeeeee;
  --quote:#9a9a9a;
  --rule:#3a3a3a;
  --link:#3a7bd5;
  --terms:#6fa3d8;
  --input:#d4d4d4;
  --button:#555555;
  --rss:#f08a24;
  --heart:#d9352a;
}
*{margin:0;padding:0;box-sizing:border-box}
html,body{width:1200px;height:717px;overflow:hidden;background:var(--page)}
body{position:relative;font-family:"Roboto",Arial,sans-serif}
.wrap{position:absolute;left:163px;width:874px;top:0;height:100%}
.band{position:absolute;left:0;width:1200px}
.services{top:0;height:384px;background:var(--page)}
.footer{top:384px;height:258px;background:var(--footer)}
.base{top:642px;height:75px;background:var(--base)}
.abs{position:absolute}
.section-title{font-family:"Gelasio",Georgia,serif;font-weight:400;font-size:24px;color:var(--ink);left:0;top:20px}
.side-rule{left:595px;top:111px;width:279px;height:3px;background:var(--ink)}
.service{position:absolute;width:250px}
.service svg{position:absolute;left:0;top:-6px}
.service .text{position:absolute;left:52px;top:0;width:200px}
.service h3{font-size:13.5px;font-weight:700;color:var(--ink);line-height:18px;margin-bottom:3px;letter-spacing:.2px}
.service p{font-size:11.5px;color:var(--body);line-height:20.5px}
.service a{display:block;font-size:11.5px;color:var(--ink);text-decoration:none;line-height:20.5px}
.col-title{font-family:"Gelasio",Georgia,serif;font-weight:400;font-size:20px;color:#fff;top:28px}
.quote{font-family:"Lora",Georgia,serif;font-style:italic;font-size:14px;line-height:18.5px;color:var(--quote);left:298px;top:67px;width:250px}
.author{font-family:"Gelasio",Georgia,serif;font-style:italic;font-weight:700;font-size:11px;color:#fff;left:298px;top:164px}
.sub-row{left:595px;width:279px;display:flex;align-items:center;gap:8px;color:#fff;font-weight:700;font-size:12.5px}
.sub-divider{left:595px;top:103px;width:279px;height:1px;background:var(--rule)}
.sub-note{left:595px;top:139px;width:279px;font-size:10.5px;line-height:18.5px;color:var(--footer-text)}
.sub-form{left:595px;top:186px;display:flex;align-items:center;gap:4px}
.sub-form label{font-size:10.5px;font-weight:700;color:#fff}
.sub-form .field{width:151px;height:23px;background:var(--input);border:1px solid #999}
.sub-form .btn{width:63px;height:23px;background:var(--button);color:#fff;font-family:"Gelasio",Georgia,serif;font-size:12.5px;display:flex;align-items:center;justify-content:center}
.copyright{left:0;top:15px;font-size:11.5px;color:#999}
.copyright a{color:var(--link)}
.terms{right:0;top:12px;font-size:10px;color:var(--terms)}
.host{left:0;top:42px;font-size:11.5px;color:#888}
.host a{color:var(--link)}
</style>
</head>
<body>

<section class="band services">
  <div class="wrap">
    <h2 class="abs section-title">Service</h2>
    <div class="abs side-rule"></div>

    <article class="service" style="left:0;top:77px">
      <svg width="40" height="36" viewBox="0 0 40 36" aria-hidden="true"><path d="M20 34 C4 22 1 15 2 10 C3 4 8 1 12 1 C16 1 19 4 20 7 C21 4 24 1 28 1 C32 1 37 4 38 10 C39 15 36 22 20 34Z" fill="var(--heart)"/></svg>
      <div class="text"><h3>Service 02</h3><p>Porem ipsum dolor sit amet, consectetuer adipiscing elit. Praesent aliquam, justo convallis luctus rutrum, erat nulla fermentum diam</p><a href="#">Read More</a></div>
    </article>

    <article class="service" style="left:279px;top:77px">
      <svg width="40" height="42" viewBox="0 0 40 42" aria-hidden="true"><rect x="2" y="4" width="28" height="36" fill="#f4f4f4" stroke="#888"/><path d="M7 14h18M7 20h18M7 26h14M7 32h10" stroke="#aaa"/><path d="M14 30 L34 6 L38 10 L18 34 L12 36Z" fill="#e8c43a" stroke="#7a6a20"/><path d="M34 6 L38 10 L40 7 L37 3Z" fill="#d9352a"/></svg>
      <div class="text"><h3>Service 02</h3><p>Porem ipsum dolor sit amet, consectetuer adipiscing elit. Praesent aliquam, justo convallis luctus rutrum, erat nulla fermentum diam</p><a href="#">Read More</a></div>
    </article>

    <article class="service" style="left:0;top:232px">
      <svg width="40" height="36" viewBox="0 0 40 36" aria-hidden="true"><path d="M20 34 C4 22 1 15 2 10 C3 4 8 1 12 1 C16 1 19 4 20 7 C21 4 24 1 28 1 C32 1 37 4 38 10 C39 15 36 22 20 34Z" fill="var(--heart)"/></svg>
      <div class="text"><h3>Service 03</h3><p>Porem ipsum dolor sit amet, consectetuer adipiscing elit. Praesent aliquam, justo convallis luctus rutrum, erat nulla fermentum diam</p><a href="#">Read More</a></div>
    </article>

    <article class="service" style="left:279px;top:232px">
      <svg width="40" height="42" viewBox="0 0 40 42" aria-hidden="true"><rect x="2" y="4" width="28" height="36" fill="#f4f4f4" stroke="#888"/><path d="M7 14h18M7 20h18M7 26h14M7 32h10" stroke="#aaa"/><path d="M14 30 L34 6 L38 10 L18 34 L12 36Z" fill="#e8c43a" stroke="#7a6a20"/><path d="M34 6 L38 10 L40 7 L37 3Z" fill="#d9352a"/></svg>
      <div class="text"><h3>Service 04</h3><p>Porem ipsum dolor sit amet, consectetuer adipiscing elit. Praesent aliquam, justo convallis luctus rutrum, erat nulla fermentum diam</p><a href="#">Read More</a></div>
    </article>
  </div>
</section>

<footer class="band footer">
  <div class="wrap">
    <h2 class="abs col-title" style="left:0">Latest Posts</h2>
    <h2 class="abs col-title" style="left:298px">Testimonials</h2>
    <h2 class="abs col-title" style="left:595px">Subscribe Now</h2>

    <blockquote class="abs quote">"Donec et ipsum et sapien vehicula nonummy. Suspendisse potenti. Fusce varius urna id quam. Sed neque mi, varius eget, tincidunt Sed neque mi, varius eget"</blockquote>
    <p class="abs author">By Marta Lindqvist, USA</p>

    <div class="abs sub-row" style="top:70px">
      <svg width="24" height="24" viewBox="0 0 26 26" aria-hidden="true"><rect x="1" y="1" width="24" height="24" rx="4" fill="var(--rss)"/><circle cx="7" cy="19" r="2.5" fill="#fff"/><path d="M5 12a9 9 0 0 1 9 9M5 6a15 15 0 0 1 15 15" stroke="#fff" stroke-width="3" fill="none"/></svg>
      <span>RSS FEED</span>
    </div>
    <div class="abs sub-divider"></div>
    <div class="abs sub-row" style="top:109px">
      <svg width="26" height="22" viewBox="0 0 28 24" aria-hidden="true"><path d="M2 10 L14 2 L26 10 V22 H2Z" fill="#e6e6e6" stroke="#999"/><path d="M2 10 L14 17 L26 10" fill="none" stroke="#999"/></svg>
      <span>Subcribe via Email</span>
    </div>
    <p class="abs sub-note">If you did like to stay updated with all our latest news please enter your e-mail address here</p>
    <div class="abs sub-form">
      <label>Email :</label>
      <div class="field"></div>
      <div class="btn">Subscribe</div>
    </div>
  </div>
</footer>

<div class="band base">
  <div class="wrap">
    <p class="abs copyright">© 2013 Willowbrook <a href="#">Care</a> Practitioners Inc All right reserved.</p>
    <p class="abs terms">Terms of Use</p>
    <p class="abs host">Brightnest <a href="#">hosting</a></p>
  </div>
</div>

</body>
</html>
```